Brivolo ( A new twist on task management )

We need modern, elegant, and clean (Quillon Design) on screens, buttons, and icons.

It is a (smart) task management application which helps the users to get notified and track task completion hassle free; Using notification profiles they create.

The interface of this application should be very simple and color schemes should be contemporary as long as they don’t make reading short text hard.

Following Quillon Design guidelines, the prefered font style is Roboto

Target Market(s)

Everyone from 13+

Industry/Entity Type

Software

Logo Text

Brivolo

Font styles to use
Other font styles liked:
• Roboto

```html
<!DOCTYPE html>
<html lang="en">
<head>
<meta charset="utf-8">
<title>Brivolo – Active Tasks</title>
<link rel="stylesheet" href="https://fonts.googleapis.com/css2?family=Roboto:wght@400;500&display=swap">
<style>
  :root {
    --status-bar: #00a5bc;
    --app-bar: #00bcd4;
    --tab-indicator: #e6ee9c;
    --on-primary: #ffffff;
    --tab-inactive: rgba(255,255,255,0.72);
    --screen-bg: #f5f5f5;
    --section-bg: #eeeeee;
    --card-bg: #ffffff;
    --text-main: #616161;
    --text-muted: #8a8a8a;
    --icon: #9e9e9e;
    --nav-bar: #000000;
    --fab: #00bcd4;
    --avatar: #8a7a66;
  }
  * { box-sizing: border-box; margin: 0; padding: 0; }
  html, body { width: 675px; height: 1200px; overflow: hidden; }
  body { font-family: 'Roboto', sans-serif; background: var(--screen-bg); position: relative; color: var(--text-main); }

  .status-bar { position: absolute; top: 0; left: 0; width: 675px; height: 45px; background: var(--status-bar); color: var(--on-primary); }
  .status-icons { position: absolute; right: 15px; top: 10px; display: flex; align-items: center; gap: 8px; font-size: 20px; }

  .app-bar { position: absolute; top: 45px; left: 0; width: 675px; height: 150px; background: var(--app-bar); box-shadow: 0 2px 4px rgba(0,0,0,0.2); z-index: 2; }
  .avatar { position: absolute; left: 25px; top: 16px; width: 58px; height: 58px; border-radius: 50%; background: radial-gradient(circle at 50% 40%, #a08a70, #5c5044); }
  .user-name { position: absolute; left: 103px; top: 30px; font-size: 26px; color: var(--on-primary); }
  .action { position: absolute; top: 28px; }
  .action.search { left: 536px; }
  .action.filter { left: 613px; }

  .tabs { position: absolute; left: 0; top: 103px; width: 675px; height: 47px; display: flex; }
  .tab { flex: 1; text-align: center; font-size: 20px; letter-spacing: 0.5px; padding-top: 11px; color: var(--tab-inactive); position: relative; }
  .tab.active { color: var(--on-primary); }
  .tab.active::after { content: ""; position: absolute; left: 0; right: 0; bottom: 0; height: 3px; background: var(--tab-indicator); }

  .section-title { position: absolute; top: 195px; left: 0; width: 675px; height: 71px; background: var(--section-bg); text-align: center; line-height: 73px; font-size: 25px; color: var(--text-main); }

  .task-list { position: absolute; top: 286px; left: 25px; width: 625px; list-style: none; }
  .task-card { height: 79px; margin-bottom: 11px; background: var(--card-bg); border-radius: 2px; box-shadow: 0 1px 2px rgba(0,0,0,0.18); position: relative; }
  .task-card .play { position: absolute; left: 21px; top: 28px; }
  .task-name { position: absolute; left: 63px; top: 0; line-height: 79px; font-size: 24px; }
  .meta-icon { position: absolute; top: 26px; }
  .meta-icon.slot-a { left: 525px; }
  .meta-icon.slot-b { left: 579px; }

  .task-card.running .stop { position: absolute; left: 20px; top: 27px; width: 26px; height: 26px; background: var(--icon); border-radius: 2px; }
  .task-card.running .skip { position: absolute; left: 64px; top: 26px; }
  .task-card.running .task-name { left: 109px; top: 12px; line-height: 30px; }
  .elapsed { position: absolute; left: 109px; top: 45px; font-size: 17px; color: var(--text-muted); }

  .fab { position: absolute; left: 573px; top: 1007px; width: 77px; height: 77px; border-radius: 50%; background: var(--fab); box-shadow: 0 3px 6px rgba(0,0,0,0.25); display: flex; align-items: center; justify-content: center; }

  .nav-bar { position: absolute; left: 0; top: 1109px; width: 675px; height: 91px; background: var(--nav-bar); display: flex; justify-content: space-around; align-items: center; padding: 0 80px; }
</style>
</head>
<body>
  <div class="status-bar">
    <div class="status-icons">
      <svg width="28" height="22" viewBox="0 0 28 22"><path d="M14 21 L0 5 Q14 -5 28 5 Z" fill="#fff"/></svg>
      <svg width="22" height="22" viewBox="0 0 22 22"><path d="M22 0 V22 H0 Z" fill="#fff"/></svg>
      <svg width="14" height="24" viewBox="0 0 14 24"><rect x="0" y="3" width="14" height="21" rx="1" fill="#fff"/><rect x="4" y="0" width="6" height="4" fill="#fff"/></svg>
      <span>12:30</span>
    </div>
  </div>

  <header class="app-bar">
    <div class="avatar" role="img" aria-label="User profile photo"></div>
    <div class="user-name">Jhon Doe</div>
    <svg class="action search" width="36" height="36" viewBox="0 0 36 36" fill="none" stroke="#fff" stroke-width="3" stroke-linecap="round"><circle cx="15" cy="15" r="11"/><line x1="23" y1="23" x2="33" y2="33"/></svg>
    <svg class="action filter" width="38" height="36" viewBox="0 0 38 36" fill="none" stroke="#fff" stroke-width="2.5"><line x1="1" y1="7" x2="37" y2="7"/><line x1="1" y1="18" x2="37" y2="18"/><line x1="1" y1="29" x2="37" y2="29"/><circle cx="25" cy="7" r="4" fill="#00bcd4"/><circle cx="13" cy="18" r="4" fill="#00bcd4"/><circle cx="25" cy="29" r="4" fill="#00bcd4"/></svg>
    <nav class="tabs">
      <div class="tab active">TASKS</div>
      <div class="tab">PROFILES</div>
    </nav>
  </header>

  <div class="section-title">Active Tasks</div>

  <svg width="0" height="0" style="position:absolute">
    <defs>
      <symbol id="i-play" viewBox="0 0 24 26"><path d="M2 2 L22 13 L2 24 Z" fill="none" stroke="#9e9e9e" stroke-width="2" stroke-linejoin="round"/></symbol>
      <symbol id="i-pin" viewBox="0 0 28 28"><path d="M17 2 L26 11 L23 12 L18 17 L18 22 L16 23 L5 12 L6 10 L11 10 L16 5 Z" fill="#9e9e9e"/><line x1="9" y1="19" x2="2" y2="26" stroke="#9e9e9e" stroke-width="2.5"/></symbol>
      <symbol id="i-place" viewBox="0 0 28 28"><path d="M14 2 C9 2 6 6 6 10 C6 16 14 22 14 22 C14 22 22 16 22 10 C22 6 19 2 14 2 Z" fill="#9e9e9e"/><circle cx="14" cy="10" r="3" fill="#fff"/><path d="M6 20 C2 21 1 23 2 24 C4 27 24 27 26 24 C27 23 26 21 22 20" fill="none" stroke="#9e9e9e" stroke-width="2"/></symbol>
      <symbol id="i-clock" viewBox="0 0 28 28"><circle cx="14" cy="14" r="12" fill="none" stroke="#9e9e9e" stroke-width="2"/><path d="M14 7 V14 H19" fill="none" stroke="#9e9e9e" stroke-width="2"/></symbol>
    </defs>
  </svg>

  <ul class="task-list">
    <li class="task-card"><svg class="play" width="24" height="26"><use href="#i-play"/></svg><span class="task-name">Task 1</span><svg class="meta-icon slot-a" width="28" height="28"><use href="#i-pin"/></svg><svg class="meta-icon slot-b" width="28" height="28"><use href="#i-place"/></svg></li>
    <li class="task-card"><svg class="play" width="24" height="26"><use href="#i-play"/></svg><span class="task-name">Task 2</span><svg class="meta-icon slot-a" width="28" height="28"><use href="#i-pin"/></svg><svg class="meta-icon slot-b" width="28" height="28"><use href="#i-place"/></svg></li>
    <li class="task-card"><svg class="play" width="24" height="26"><use href="#i-play"/></svg><span class="task-name">Task 3</span><svg class="meta-icon slot-a" width="28" height="28"><use href="#i-clock"/></svg><svg class="meta-icon slot-b" width="28" height="28"><use href="#i-place"/></svg></li>
    <li class="task-card"><svg class="play" width="24" height="26"><use href="#i-play"/></svg><span class="task-name">Task 4</span><svg class="meta-icon slot-a" width="28" height="28"><use href="#i-pin"/></svg><svg class="meta-icon slot-b" width="28" height="28"><use href="#i-place"/></svg></li>
    <li class="task-card"><svg class="play" width="24" height="26"><use href="#i-play"/></svg><span class="task-name">Task 5</span><svg class="meta-icon slot-b" width="28" height="28"><use href="#i-clock"/></svg></li>
    <li class="task-card"><svg class="play" width="24" height="26"><use href="#i-play"/></svg><span class="task-name">Task 6</span><svg class="meta-icon slot-a" width="28" height="28"><use href="#i-pin"/></svg><svg class="meta-icon slot-b" width="28" height="28"><use href="#i-place"/></svg></li>
    <li class="task-card running">
      <span class="stop"></span>
      <svg class="skip" width="28" height="28" viewBox="0 0 28 28"><path d="M0 2 L20 14 L0 26 Z" fill="#9e9e9e"/><rect x="22" y="2" width="4" height="24" fill="#9e9e9e"/></svg>
      <span class="task-name">Task 7</span>
      <span class="elapsed">00h:15m:56s</span>
      <svg class="meta-icon slot-b" width="28" height="28"><use href="#i-place"/></svg>
    </li>
  </ul>

  <div class="fab" aria-label="Add task">
    <svg width="26" height="26" viewBox="0 0 26 26" stroke="#fff" stroke-width="2"><line x1="13" y1="1" x2="13" y2="25"/><line x1="1" y1="13" x2="25" y2="13"/></svg>
  </div>

  <nav class="nav-bar">
    <svg width="34" height="36" viewBox="0 0 34 36" fill="none" stroke="#fff" stroke-width="3" stroke-linejoin="round"><path d="M31 3 L31 33 L3 18 Z"/></svg>
    <svg width="36" height="36" viewBox="0 0 36 36" fill="none" stroke="#fff" stroke-width="3"><circle cx="18" cy="18" r="15"/></svg>
    <svg width="32" height="32" viewBox="0 0 32 32" fill="none" stroke="#fff" stroke-width="3"><rect x="2" y="2" width="28" height="28"/></svg>
  </nav>
</body>
</html>
```